Corporate WordPress Site for Global IT Staffing Firm

We are looking for a corporate web presence for our company, Quillex, that is an IT Staffing and Recruiting firm based in Silicon Valley. We want the site to convey strength, confidence and trust in our F500 global customers and be appealing to prospective job seekers looking for their next employment.
I've attached the logo scheme to you. I can provide content within the next few days as well as links to our Chirply, PB pages. I also have wallpaper images selected from Marrow stills for a scrolling banner. Eventually we'll post job openings with search capabilities from a third party VMS SaaS company called Tidewick.
Target Market(s)
Global 1000 companies who purchase staffing from our firm AND prospective job seekers looking for work.
Industry/Entity Type
It Company
Number of Pages Required
3 page
Requirements
Must have
- Modern, parallax design for corporate image. May need links and integration to third party systems in a few months.
- Want each of the images via slider or images to convey:
- Attention to Detail
- Taking the Time to Find the Right Candidates
- Old Fashioned Hard Work
- Assembling the Right Teams
- Built to Scale
Nice to have
- Sliders. Counters. Links to social media pages. Background information. Bio pages. Reference customers.
- Examples of sites we like.
- https://www.rydexo.example/
- http://www.palvinmediaset.example/
- http://www.qornaworks.example/

```html
<!DOCTYPE html>
<html lang="en">
<head>
<meta charset="utf-8">
<title>Quillex — IT Staffing and Recruiting</title>
<link href="https://fonts.googleapis.com/css2?family=Lato:wght@300;400;700;900&family=Lora:ital@1&display=swap" rel="stylesheet">
<style>
  :root{
    --accent:#4d6b9a;
    --accent-dark:#3e5a86;
    --ink:#3a3a3a;
    --muted:#7a7a7a;
    --white:#ffffff;
    --footer-bg:#f1f1f1;
    --line:#d8d8d8;
  }
  *{margin:0;padding:0;box-sizing:border-box}
  html,body{width:1200px;height:2303px;overflow:hidden}
  body{font-family:'Lato',Arial,sans-serif;color:var(--ink);background:var(--white);position:relative}
  .abs{position:absolute}

  /* Hero */
  .hero{position:absolute;left:0;top:0;width:1200px;height:635px;overflow:hidden}
  .hero-photo{position:absolute;inset:0;background:
      radial-gradient(ellipse at 50% 80%, #a87d5e 0%, rgba(168,125,94,0) 30%),
      linear-gradient(135deg,#d7dce3 0%,#8f9aaa 35%,#5a6576 60%,#2f3848 100%)}
  .hero-shade{position:absolute;inset:0;background:rgba(30,40,60,.28)}
  .brand{left:41px;top:22px;display:flex;align-items:center;gap:10px;color:var(--white);font-weight:900;font-size:26px;letter-spacing:.5px}
  .brand-dot{width:14px;height:14px;border-radius:50%;background:var(--white)}
  .nav{right:38px;top:20px;display:flex;align-items:center;gap:38px;color:var(--white);font-size:14px}
  .nav-cta{border:2px solid var(--white);border-radius:18px;padding:7px 26px}
  .hero-copy{left:0;width:1200px;text-align:center;color:var(--white)}
  .tagline{top:183px;font-size:12px;font-weight:700;letter-spacing:2px}
  .tagline span{margin:0 10px}
  .hero-title{top:206px;font-size:36px;font-weight:400;letter-spacing:1px;line-height:38px}
  .hero-rule{left:570px;top:302px;width:60px;height:1px;background:var(--white)}
  .hero-sub{top:330px;font-family:'Lora',Georgia,serif;font-style:italic;font-size:19px}
  .btn{left:507px;top:392px;width:184px;height:48px;border-radius:24px;background:var(--accent);color:var(--white);font-size:14px;font-weight:700;letter-spacing:1.5px;display:flex;align-items:center;justify-content:center}
  .dots{left:576px;top:573px;display:flex;gap:8px}
  .dots i{width:9px;height:9px;border-radius:50%;background:rgba(255,255,255,.5)}
  .dots i:first-child{background:var(--white)}

  /* Section heads */
  .section-title{left:0;width:1200px;text-align:center;font-size:19px;font-weight:400;letter-spacing:1.5px;color:var(--ink)}
  .section-rule{left:570px;width:60px;height:2px;background:#b8c3d4}
  .lead{left:300px;width:600px;text-align:center;font-size:13px;line-height:18px;color:var(--muted)}

  /* Feature panels */
  .panels{left:0;top:939px;width:1200px;height:397px;display:flex}
  .panel{position:relative;width:400px;height:397px;color:var(--white);text-align:center}
  .panel-photo{position:absolute;inset:0}
  .panel-1 .panel-photo{background:linear-gradient(160deg,#6d84a8 0%,#4b6590 55%,#2f4266 100%)}
  .panel-2 .panel-photo{background:linear-gradient(160deg,#b3b3b3 0%,#8c8c8c 50%,#5d5d5d 100%)}
  .panel-3 .panel-photo{background:linear-gradient(160deg,#7d95b8 0%,#5b76a0 50%,#34496e 100%)}
  .panel-body{position:absolute;left:40px;right:40px;top:126px}
  .panel-title{font-size:17px;font-weight:700;letter-spacing:1px;margin-bottom:30px}
  .panel-text{font-size:12px;line-height:18px;margin-bottom:20px}
  .panel-link{font-family:'Lora',Georgia,serif;font-style:italic;font-size:13px}

  /* Steps */
  .steps{left:0;top:1640px;width:1200px;display:flex;justify-content:center;gap:0}
  .step{width:360px;text-align:center}
  .step-icon{width:92px;height:92px;border-radius:50%;background:var(--accent);margin:0 auto;display:flex;align-items:center;justify-content:center}
  .step-title{margin-top:64px;font-size:15px;font-weight:700;letter-spacing:.8px}
  .step-rule{width:40px;height:2px;background:#b8c3d4;margin:14px auto 20px}
  .step-text{width:270px;margin:0 auto;font-size:12px;line-height:18px;color:var(--muted)}

  /* Footer */
  .footer{left:0;top:2042px;width:1200px;height:261px;background:var(--footer-bg)}
  .foot-head{font-size:10px;font-weight:700;letter-spacing:1px;color:#666;top:61px}
  .foot-text{font-size:10px;line-height:17px;color:#999;top:84px}
  .foot-brand{left:896px;top:46px;display:flex;align-items:center;gap:8px;color:#8a8a8a;font-weight:900;font-size:18px}
  .foot-brand-dot{width:12px;height:12px;border-radius:50%;background:#8a8a8a}
  .foot-rule{left:77px;top:184px;width:1046px;height:1px;background:var(--line)}
  .foot-copy{left:77px;top:203px;font-size:10px;color:#999}
  .social{left:1068px;top:200px;display:flex;gap:12px}
  .social i{width:11px;height:11px;border-radius:2px;background:#9a9a9a}
</style>
</head>
<body>

<header class="hero">
  <div class="hero-photo" role="img" aria-label="Photograph of business people stacking hands together over an office desk"></div>
  <div class="hero-shade"></div>
  <div class="abs brand"><span class="brand-dot"></span>Quillex</div>
  <nav class="abs nav">
    <span>About</span><span>Services</span><span>Contact</span>
    <span class="nav-cta">Search Jobs</span>
  </nav>
  <p class="abs hero-copy tagline">STRENGTH<span>•</span>CONFIDENCE<span>•</span>TRUST</p>
  <h1 class="abs hero-copy hero-title">IT STAFFING AND RECRUITING<br>MADE EASY</h1>
  <div class="abs hero-rule"></div>
  <p class="abs hero-copy hero-sub">Lorem Ipsum is simply dummy text of the printing and typesetting industry</p>
  <div class="abs btn">HOW IT WORKS</div>
  <div class="abs dots"><i></i><i></i><i></i></div>
</header>

<h2 class="abs section-title" style="top:707px">A SAMPLE HEADLINE LOREM IPSUM</h2>
<div class="abs section-rule" style="top:757px"></div>
<p class="abs lead" style="top:784px">Lorem ipsum dolor sit amet, sed do eiusmod tempor incididunt ut labore et dolore magna. Quis nostrud exercitation ullamco laboris nisi ut aliquip ex ea commodo consequat. Duis aute irure dolor in in voluptate velit esse cillum dolore eu fugiat. Excepteur sint cupidatat non proident, sunt in culpa qui officia deserunt mollit anim id est laborum.</p>

<section class="abs panels">
  <article class="panel panel-1">
    <div class="panel-photo" role="img" aria-label="Photograph of rows of light bulbs with a blue tint"></div>
    <div class="panel-body">
      <h3 class="panel-title">WHY CHOOSE QUILLEX</h3>
      <p class="panel-text">Lorem Ipsum is simply dummy text of the printing and typesetting industry. It has been the industry's</p>
      <p class="panel-link">find out more</p>
    </div>
  </article>
  <article class="panel panel-2">
    <div class="panel-photo" role="img" aria-label="Black and white photograph of a hand holding a measuring tape"></div>
    <div class="panel-body">
      <h3 class="panel-title">OUR EDGE</h3>
      <p class="panel-text">Lorem Ipsum is simply dummy text of the printing and typesetting industry. It has been the industry's</p>
      <p class="panel-link">find out more</p>
    </div>
  </article>
  <article class="panel panel-3">
    <div class="panel-photo" role="img" aria-label="Photograph of a person searching on a laptop, blue tinted"></div>
    <div class="panel-body">
      <h3 class="panel-title">SEARCH JOBS</h3>
      <p class="panel-text">Lorem Ipsum is simply dummy text of the printing and typesetting industry. It has been the industry's</p>
      <p class="panel-link">find out more</p>
    </div>
  </article>
</section>

<h2 class="abs section-title" style="top:1429px">HOW QUILLEX WORKS</h2>
<div class="abs section-rule" style="top:1468px"></div>
<p class="abs lead" style="top:1505px">Lorem ipsum dolor sit amet, sed do eiusmod tempor incididunt ut labore et dolore magna. Quis nostrud exercitation ullamco laboris nisi ut aliquip ex ea commodo consequat.</p>

<section class="abs steps">
  <div class="step">
    <div class="step-icon">
      <svg width="30" height="40" viewBox="0 0 30 40"><path d="M15 0C6.7 0 0 6.7 0 15c0 11 15 25 15 25s15-14 15-25C30 6.7 23.3 0 15 0z" fill="#fff"/><circle cx="15" cy="15" r="5.5" fill="#4d6b9a"/></svg>
    </div>
    <h3 class="step-title">LOREM IPSUM DOLOR</h3>
    <div class="step-rule"></div>
    <p class="step-text">Sed ut perspiciatis unde omnis iste natus error sit voluptatem accusantium doloremque laudantium, totam rem aperiam, eaque ipsa quae ab illo.</p>
  </div>
  <div class="step">
    <div class="step-icon">
      <svg width="42" height="34" viewBox="0 0 42 34"><circle cx="15" cy="9" r="8" fill="#fff"/><path d="M0 34c0-9 6.7-14 15-14s15 5 15 14z" fill="#fff"/><circle cx="30" cy="8" r="6" fill="#fff"/><path d="M32 17c6 1 10 5 10 12h-9c0-5-1-9-4-12z" fill="#fff"/></svg>
    </div>
    <h3 class="step-title">LOREM IPSUM DOLOR</h3>
    <div class="step-rule"></div>
    <p class="step-text">Sed ut perspiciatis unde omnis iste natus error sit voluptatem accusantium doloremque laudantium, totam rem aperiam, eaque ipsa quae ab illo.</p>
  </div>
  <div class="step">
    <div class="step-icon">
      <svg width="38" height="38" viewBox="0 0 38 38"><circle cx="15" cy="15" r="11" fill="none" stroke="#fff" stroke-width="5"/><line x1="23" y1="23" x2="35" y2="35" stroke="#fff" stroke-width="6" stroke-linecap="round"/></svg>
    </div>
    <h3 class="step-title">LOREM IPSUM DOLOR</h3>
    <div class="step-rule"></div>
    <p class="step-text">Sed ut perspiciatis unde omnis iste natus error sit voluptatem accusantium doloremque laudantium, totam rem aperiam, eaque ipsa quae ab illo.</p>
  </div>
</section>

<footer class="abs footer">
  <h4 class="abs foot-head" style="left:77px">ABOUT QUILLEX</h4>
  <p class="abs foot-text" style="left:77px;width:200px">Sed ut perspiciatis unde omnis iste natus error sit voluptatem accusantium doloremque laudantium, totam rem aperiam</p>
  <p class="abs foot-text" style="left:294px;width:200px">Sed ut perspiciatis unde omnis iste natus error sit voluptatem accusantium doloremque laudantium, totam rem aperiam</p>
  <h4 class="abs foot-head" style="left:548px">CONTACT US</h4>
  <p class="abs foot-text" style="left:548px;width:240px">+1 555 010 2030 or +1 555 010 4040<br>info@quillex.example<br>120 Bay Street, Santa Clara, CA</p>
  <div class="abs foot-brand"><span class="foot-brand-dot"></span>Quillex</div>
  <p class="abs foot-text" style="left:896px;width:230px">Quillex is a talent partner for global teams seeking skilled engineers.</p>
  <div class="abs foot-rule"></div>
  <p class="abs foot-copy">Copyright © 2015 Quillex &nbsp;|&nbsp; Terms &amp; Conditions &nbsp;|&nbsp; Sitemap &nbsp;|&nbsp; Contact</p>
  <div class="abs social" aria-label="Social links"><i></i><i></i><i></i></div>
</footer>

</body>
</html>
```